4 x Designs Required

Hi There,
I require 4 x different designs to be made for 4 new brands of mine however they can be quite interchangeable. HR Plinkr and Marketing Plinkr can be similar just with a difference in colour. The same goes for the Bulletin brands. This means there are ultimately two designs that need perfecting.

There must be a click here CTA on the banner somewhere. :-)

I require the banners in 728x90 format and 960x90 please.

Please use strap lines on the banners such as:
Essential Whitepapers for HR Professionals
Essential Whitepapers for Marketing Professionals
Your No.1 Whitepaper Resource

The brand names:
HR Plinkr
Marketing Plinkr
HR Dispatchly
Marketing Dispatchly

Examples attached.

```html
<!DOCTYPE html>
<html lang="en">
<head>
<meta charset="utf-8">
<title>Whitepaper Banners – Plinkr &amp; Dispatchly</title>
<link rel="stylesheet" href="https://fonts.googleapis.com/css2?family=Lato:wght@700&family=Montserrat:wght@600&family=Oswald:wght@500;600&display=swap">
<style>
  :root {
    --backdrop: #8b8b8b;
    --backdrop-dark: #3a3a3a;
    --ink: #ffffff;
    --black: #0a0c0d;
    --teal: #2aa9c4;
    --orange: #ef7a12;
    --navy: #0b1842;
    --navy-deep: #081033;
    --red: #d91a10;
    --red-dark: #3a0503;
    --purple: #2a0a4a;
    --purple-deep: #14052a;
    --green: #1fb47a;
  }
  * { margin: 0; padding: 0; box-sizing: border-box; }
  html, body { width: 1200px; height: 622px; overflow: hidden; }
  body {
    background: radial-gradient(ellipse 60% 55% at 42% 50%, var(--backdrop-dark) 0%, #5e5e5e 55%, var(--backdrop) 100%);
  }
  .stage {
    position: relative;
    width: 1132px; height: 587px;
    transform: scale(1.0601);
    transform-origin: 0 0;
  }
  .banner {
    position: absolute; left: 86px; height: 90px; overflow: hidden;
    box-shadow: 0 10px 40px rgba(0,0,0,.45);
  }
  .banner--728 { width: 728px; }
  .banner--960 { width: 960px; }
  .banner > * { position: absolute; }
  .photo { inset: 0; }
  .strap {
    font-family: "Oswald", sans-serif; font-weight: 600;
    font-size: 21px; line-height: 31px; color: var(--ink);
    text-shadow: 0 1px 3px rgba(0,0,0,.6);
    letter-spacing: -0.2px;
    white-space: nowrap;
  }
  .strap--round {
    font-family: "Montserrat", sans-serif; font-size: 23px; line-height: 29px;
    letter-spacing: 0;
  }
  .brand {
    font-family: "Lato", sans-serif; font-weight: 700; color: var(--ink);
    white-space: nowrap;
  }
  .cta {
    display: flex; align-items: center; justify-content: center;
    font-family: "Oswald", sans-serif; font-weight: 500; color: var(--ink);
    text-transform: uppercase; letter-spacing: -0.2px;
  }

  /* HR Plinkr */
  .plinkr-hr { top: 88px; background: var(--black); }
  .plinkr-hr .photo {
    left: 190px;
    background: radial-gradient(circle at 20% 75%, #5b4a3c 0%, transparent 30%),
                radial-gradient(circle at 70% 40%, #5a1a12 0%, transparent 35%),
                radial-gradient(circle at 90% 60%, #6b3a10 0%, transparent 30%),
                linear-gradient(90deg, #1a1c1e, #121212 60%, #1c0c08);
  }
  .plinkr-hr .curve { left: 0; top: 0; }
  .plinkr-hr .brand { left: 12px; top: 24px; font-size: 32px; }
  .plinkr-hr .strap { left: 244px; top: 14px; }
  .plinkr-hr .cta {
    left: 623px; top: 40px; width: 99px; height: 43px;
    background: var(--orange); border-radius: 22px; font-size: 15px;
  }

  /* Marketing Plinkr */
  .plinkr-mkt { top: 195px; background: var(--navy); }
  .plinkr-mkt .photo {
    right: 210px; left: 0;
    background: radial-gradient(circle at 60% 70%, #7a4a38 0%, transparent 28%),
                radial-gradient(circle at 88% 30%, #2f6fb0 0%, transparent 30%),
                linear-gradient(90deg, var(--navy-deep), #1a2a68 70%, #24407e);
  }
  .plinkr-mkt .panel { right: 0; top: 0; width: 228px; height: 90px; }
  .plinkr-mkt .brand { left: 540px; top: 11px; font-size: 33px; line-height: 34px; }
  .plinkr-mkt .strap { left: 24px; top: 11px; }
  .plinkr-mkt .cta {
    left: 376px; top: 55px; width: 83px; height: 35px;
    background: var(--orange); font-size: 13px;
  }

  /* HR Dispatchly */
  .dispatch-hr { top: 302px; background: #050000; }
  .dispatch-hr .photo {
    background: radial-gradient(ellipse 25% 80% at 10% 50%, var(--red-dark), transparent),
                radial-gradient(ellipse 30% 90% at 90% 50%, #4a0604, transparent),
                #060000;
  }
  .dispatch-hr .brand { left: 20px; top: 26px; font-size: 32px; }
  .dispatch-hr .strap { left: 289px; top: 14px; }
  .dispatch-hr .cta {
    left: 707px; top: 24px; width: 99px; height: 43px;
    background: var(--red); font-size: 15px;
  }

  /* Marketing Dispatchly */
  .dispatch-mkt { top: 409px; background: var(--purple-deep); }
  .dispatch-mkt .photo {
    background: radial-gradient(ellipse 20% 90% at 12% 100%, #5a1a9a, transparent),
                radial-gradient(ellipse 12% 100% at 84% 50%, #4a1290, transparent),
                linear-gradient(90deg, var(--purple), #1e0838 60%, var(--purple-deep));
  }
  .dispatch-mkt .brand { left: 742px; top: 11px; font-size: 34px; line-height: 34px; }
  .dispatch-mkt .strap { left: 26px; top: 15px; }
  .dispatch-mkt .cta {
    left: 530px; top: 56px; width: 107px; height: 34px;
    background: var(--green); border-radius: 22px 0 0 0; font-size: 13px;
  }
</style>
</head>
<body>
<main class="stage">

  <section class="banner banner--728 plinkr-hr">
    <div class="photo" role="img" aria-label="Dark photo of a glowing globe with warm bokeh lights"></div>
    <svg class="curve" width="230" height="90" viewBox="0 0 230 90" aria-hidden="true">
      <path d="M0 0H184Q234 45 184 90H0Z" fill="var(--black)"/>
      <path d="M184 0Q234 45 184 90L190 90Q242 45 190 0Z" fill="var(--teal)"/>
    </svg>
    <div class="brand">HR Plinkr</div>
    <p class="strap">Essential Whitepapers for HR Professionals<br>Your No.1 Whitepaper Resource</p>
    <div class="cta">Click Here</div>
  </section>

  <section class="banner banner--728 plinkr-mkt">
    <div class="photo" role="img" aria-label="Blue photo of a circuit board with warm light"></div>
    <svg class="panel" width="228" height="90" viewBox="0 0 228 90" aria-hidden="true">
      <path d="M24 0H228V90H24Q-6 45 24 0Z" fill="var(--navy-deep)"/>
      <path d="M24 0Q-6 45 24 90L18 90Q-14 45 18 0Z" fill="var(--orange)"/>
    </svg>
    <p class="strap">Essential Whitepapers for Marketing Professionals<br>Your No.1 Whitepaper Resource</p>
    <div class="cta">Click Here</div>
    <div class="brand">Marketing<br>Plinkr</div>
  </section>

  <section class="banner banner--960 dispatch-hr">
    <div class="photo" role="img" aria-label="Black background with glowing red diagonal light streaks"></div>
    <div class="brand">HR Dispatchly</div>
    <p class="strap">Essential Whitepapers for HR Professionals<br>Your No.1 Whitepaper Resource</p>
    <div class="cta">Click Here</div>
  </section>

  <section class="banner banner--960 dispatch-mkt">
    <div class="photo" role="img" aria-label="Deep purple background with glowing violet wireframe and particles"></div>
    <p class="strap strap--round">Essential Whitepapers for Marketing Professionals<br>Your No.1 Whitepaper Resource</p>
    <div class="cta">Click Here</div>
    <div class="brand">Marketing<br>Dispatchly</div>
  </section>

</main>
</body>
</html>
```